Business Card Design

I need a business card design for my new solo law practice. I practice consumer bankruptcy law.

I would like a simple, functional business card that looks professional but will also be understandable to regular people - not just other lawyers.
Updates

I added a couple of possible logos that can be incorporated

I'm sorry about the confusion, but the suite number for my new office is suite #150. Thanks for your patience

Target Market(s)

the real target market is potential clients

Industry/Entity Type

Business

Contact Information for Business Card

Law Offices of Dorian P. Whitcombe
Dorian P. Whitcombe
Attorney at Law
Bankruptcy Law
487 Mariner Court #150
Larkmoor, PA 15999
(555) 318-7264 (Phone)
(555) 318-7290 (Fax)
dorianw@fernleydebtrelief.example
fernleydebtrelief.example

Font styles to use
Serif

Requirements
Nice to have
• I've added some possible logos to possible incorporate

```html
<!DOCTYPE html>
<html lang="en">
<head>
<meta charset="utf-8">
<title>Dorian P. Whitcombe – Business Card</title>
<link rel="stylesheet" href="https://fonts.googleapis.com/css2?family=Source+Sans+3:wght@400;600&display=swap">
<style>
  :root {
    --backdrop: #e4e4e6;
    --card-white: #ffffff;
    --navy: #22446b;
    --crimson: #a3161f;
    --ink-light: #ffffff;
    --ring: #22446b;
  }
  * { margin: 0; padding: 0; box-sizing: border-box; }
  html, body {
    width: 1200px; height: 564px; overflow: hidden;
    background: var(--backdrop);
    font-family: "Source Sans 3", "Myriad Pro", Arial, sans-serif;
  }
  .canvas {
    position: relative; width: 1200px; height: 564px;
    display: flex; align-items: center; justify-content: center;
  }
  .business-card {
    position: relative; width: 700px; height: 400px;
    border-radius: 24px; overflow: hidden;
    background: var(--card-white);
    box-shadow: 0 8px 24px rgba(0,0,0,.18);
  }
  .card-header { position: absolute; left: 0; top: 0; width: 100%; height: 170px; }
  .attorney-name {
    position: absolute; left: 36px; top: 96px;
    font-size: 36px; font-weight: 400; letter-spacing: .5px;
    color: var(--crimson); text-transform: uppercase; line-height: 1;
  }
  .attorney-title {
    position: absolute; left: 38px; top: 136px;
    font-size: 17px; color: var(--navy); line-height: 1;
  }
  .firm-mark {
    position: absolute; right: 22px; top: 12px; width: 220px;
    display: flex; flex-direction: column; align-items: center;
  }
  .firm-mark__circle {
    width: 128px; height: 128px; border-radius: 50%;
    border: 9px solid var(--ring);
  }
  .firm-mark__name {
    margin-top: 6px; font-size: 12.5px; font-weight: 600;
    color: var(--navy); white-space: nowrap;
  }
  .card-band {
    position: absolute; left: 0; top: 170px; width: 100%; height: 230px;
    background: var(--navy); color: var(--ink-light);
  }
  .contact-list { position: absolute; left: 30px; top: 28px; list-style: none; }
  .contact-item {
    display: flex; align-items: center; height: 42px;
    font-size: 20px; line-height: 1;
  }
  .contact-item svg { width: 18px; height: 18px; margin-right: 22px; flex: none; }
  .office-address {
    position: absolute; left: 470px; top: 40px;
    font-size: 21px; line-height: 1.35; font-style: normal;
  }
</style>
</head>
<body>
<main class="canvas">
  <article class="business-card">
    <header class="card-header">
      <h1 class="attorney-name">Dorian P. Whitcombe</h1>
      <p class="attorney-title">Attorney at Law Bankruptcy Law</p>
      <div class="firm-mark">
        <div class="firm-mark__circle"></div>
        <p class="firm-mark__name">Law Offices of Dorian P. Whitcombe</p>
      </div>
    </header>
    <section class="card-band">
      <ul class="contact-list">
        <li class="contact-item">
          <svg viewBox="0 0 18 18" aria-hidden="true"><rect x="5" y="1" width="8" height="16" rx="1.5" fill="none" stroke="#fff" stroke-width="1.6"/><circle cx="9" cy="14" r="1" fill="#fff"/></svg>
          (555) 318-7264
        </li>
        <li class="contact-item">
          <svg viewBox="0 0 18 18" aria-hidden="true"><rect x="2" y="6" width="14" height="9" rx="1.5" fill="#fff"/><rect x="5" y="2" width="8" height="5" fill="none" stroke="#fff" stroke-width="1.4"/></svg>
          (555) 318-7290
        </li>
        <li class="contact-item">
          <svg viewBox="0 0 18 18" aria-hidden="true"><rect x="1.5" y="4" width="15" height="10" rx="1" fill="#fff"/><path d="M1.5 4.5 9 10l7.5-5.5" fill="none" stroke="#22446b" stroke-width="1.3"/></svg>
          dorianw@fernleydebtrelief.example
        </li>
        <li class="contact-item">
          <svg viewBox="0 0 18 18" aria-hidden="true"><circle cx="9" cy="9" r="7.5" fill="none" stroke="#fff" stroke-width="1.5"/><ellipse cx="9" cy="9" rx="3" ry="7.5" fill="none" stroke="#fff" stroke-width="1.2"/><path d="M1.5 9h15" stroke="#fff" stroke-width="1.2"/></svg>
          www.fernleydebtrelief.example
        </li>
      </ul>
      <address class="office-address">
        487 Mariner Court<br>
        #150 Larkmoor,<br>
        PA 15999
      </address>
    </section>
  </article>
</main>
</body>
</html>
```